Brisk Morsels
Business Card and Stationary Design
Brisk Morsels -
Creative Brief
Bright & Fun-filled
Gordon T Welham
Owner
41 Harlow Lane Millbrook Ridge, NJ 08637
Gord.Welham@postmailer.example
www.brisk-morsels.example
Looking for something simple, but eye-catching. Looking for a variety of different fonts/styles/backgrounds to achieve: -Seamless integration with the attached logo. -Backgrounds to enhance the "pop" of the logo. -Professional, but with a hint of fun. The Brisk Morsel will compete in the energy drink/shot industry (e.g. Tan Lynx and Nine Minute Vigor). We differentiate ourselves through superior taste and natural ingredients, creating a more satisfying experience for the energy consumer. Feel free to message me with any questions/concerns/comments.

```html
<!DOCTYPE html>
<html lang="en">
<head>
<meta charset="utf-8">
<title>Brisk Morsels — Business Cards</title>
<link rel="stylesheet" href="https://fonts.googleapis.com/css2?family=Questrial&display=swap">
<style>
  :root {
    --stage: #ece8e3;
    --card-white: #ffffff;
    --card-orange: #f7941d;
    --card-brown: #7a5230;
    --brown-ink: #6b4526;
    --orange-ink: #f0861a;
    --grey-ink: #5a5a5a;
    --cream: #fff3e3;
  }
  * { margin: 0; padding: 0; box-sizing: border-box; }
  html, body { width: 1200px; height: 816px; overflow: hidden; }
  body {
    background: var(--stage);
    font-family: "Questrial", sans-serif;
    position: relative;
  }
  .card {
    position: absolute;
    width: 480px; height: 274px;
    border-radius: 14px;
    box-shadow: 0 6px 18px rgba(0,0,0,0.18);
    display: flex; flex-direction: column;
    align-items: center; justify-content: center;
    text-align: center;
  }
  .card--front  { left: 80px;  top: 100px; background: var(--card-white); }
  .card--orange { left: 640px; top: 100px; background: var(--card-orange); }
  .card--brown  { left: 360px; top: 440px; background: var(--card-brown); }

  .brand {
    display: inline-flex; align-items: center; gap: 10px;
    color: var(--brown-ink); font-size: 30px;
  }
  .brand__dot { width: 20px; height: 20px; border-radius: 50%; background: var(--orange-ink); }
  .card--orange .brand__dot { background: var(--cream); }
  .card--brown .brand { color: var(--cream); font-size: 40px; }
  .card--brown .brand__dot { width: 26px; height: 26px; }

  .contact { margin-top: 18px; color: var(--grey-ink); font-size: 11px; line-height: 1.6; }
  .contact__name { color: var(--orange-ink); font-size: 15px; line-height: 1.3; }
  .contact__role { font-size: 9px; margin-bottom: 10px; }
  .contact__label { color: var(--orange-ink); }
  .contact__web { margin-top: 8px; }
</style>
</head>
<body>
  <section class="card card--front">
    <div class="brand"><span class="brand__dot"></span><span class="brand__name">Brisk Morsels</span></div>
    <div class="contact">
      <div class="contact__name">Gordon T Welham</div>
      <div class="contact__role">Owner</div>
      <div class="contact__address">41 Harlow Lane, Millbrook Ridge, NJ 08637</div>
      <div><span class="contact__label">Cell:</span> (555) 014-2297 &nbsp;|&nbsp; <span class="contact__label">Email:</span> Gord.Welham@postmailer.example</div>
      <div><span class="contact__label">Email:</span> Gord.Welham@postmailer.example</div>
      <div class="contact__web">www.brisk-morsels.example</div>
    </div>
  </section>

  <section class="card card--orange">
    <div class="brand"><span class="brand__dot"></span><span class="brand__name">Brisk Morsels</span></div>
  </section>

  <section class="card card--brown">
    <div class="brand"><span class="brand__dot"></span><span class="brand__name">Brisk Morsels</span></div>
  </section>
</body>
</html>
```